Crowler Can Label for a Brewery Beer Can

Creating a label for our brewery's Crowler Can. Our area is know for mountains, glaciers, and the ocean view. We would like to include these in the drawing. Along with our logo. Overall we think more is less. A nice simple label is our preference that is elegant. We included a couple we like, but do not copy them exactly.

There will need to be white room for us to label each can by hand - spaces for - Name, ABV and Date.

The text must be on lable- GOVERNMENT WARNING: (1) According to the Surgeon General, women should not drink alcoholic beverages during pregnancy because of the risk of birth defects. (2) Consumption of alcoholic beverages impairs your ability to drive a car or operate machinery,and may cause health problems.

We also want our address and website-
267 Tamarack Ln, Kestrel Cove Alaska 99000
www.fernhollowales.com

Also needs to have size on the label - 32 Fluid Oz

Getting some great designs, but be good for more time for some designers to rework with suggestions given.

Designer to choose colors to be used in the design.

• I included the label size template in the graphics. Must be this size.
• There will need to be white room for us to label each can by hand - spaces for - Name, ABV and Date.
• The text must be on lable- GOVERNMENT WARNING: (1) According to the Surgeon General, women should not drink alcoholic beverages during pregnancy because of the risk of birth defects. (2) Consumption of alcoholic beverages impairs your ability to drive a car or operate machinery,and may cause health problems.
• We also want our address and website-
• 267 Tamarack Ln, Kestrel Cove Alaska 99000
• www.fernhollowales.com
• Needs to have size on the label - 32 Fl Oz
• Mountains, Glacier and ocean scene.

```html
<!DOCTYPE html>
<html lang="en">
<head>
<meta charset="utf-8">
<title>Fern Hollow Ales – Crowler Label</title>
<link rel="stylesheet" href="https://fonts.googleapis.com/css2?family=Arimo:wght@400;700&family=Cinzel:wght@600&family=Roboto+Slab:wght@300;400&display=swap">
<style>
  :root {
    --ink: #1d1d1d;
    --paper: #ffffff;
    --label-light: #f3f4f5;
    --label-mid: #dcdedf;
    --backdrop: #f7f7f7;
  }
  * { box-sizing: border-box; margin: 0; padding: 0; }
  html, body { width: 1200px; height: 1200px; overflow: hidden; background: var(--backdrop); }
  .sheet { position: relative; width: 1200px; height: 1200px; }

  .panel {
    position: absolute; top: 120px; width: 440px; height: 900px;
    background: linear-gradient(90deg, var(--label-mid), var(--label-light) 30%, var(--paper) 50%, var(--label-light) 70%, var(--label-mid));
    color: var(--ink);
  }
  .panel--front { left: 120px; }
  .panel--back { left: 640px; }

  /* Front */
  .brand-mark {
    position: absolute; left: 155px; top: 160px; width: 130px; height: 130px;
    border-radius: 50%; background: var(--ink);
  }
  .brand-name, .brand-sub, .brand-place {
    position: absolute; left: 0; width: 100%; text-align: center;
    font-family: "Arimo", Arial, sans-serif; font-weight: 700; white-space: nowrap;
  }
  .brand-name { top: 318px; font-size: 46px; line-height: 56px; }
  .brand-sub { top: 380px; font-size: 28px; line-height: 34px; letter-spacing: 18px; padding-left: 18px; }
  .brand-place {
    top: 428px; font-size: 17px; line-height: 22px; letter-spacing: 2px;
    display: flex; justify-content: center; align-items: center; gap: 12px;
  }
  .brand-place::before, .brand-place::after { content: ""; width: 34px; height: 2px; background: var(--ink); }

  .crowler-band {
    position: absolute; left: 44px; top: 464px; width: 352px; height: 42px;
    background: var(--ink); color: var(--paper);
    font-family: "Cinzel", Georgia, serif; font-weight: 600; font-size: 36px;
    text-align: center; line-height: 42px; letter-spacing: 1px;
  }
  .fill-box {
    position: absolute; left: 44px; top: 506px; width: 352px; height: 164px;
    background: var(--paper);
    font-family: "Arimo", Arial, sans-serif; font-size: 22px; line-height: 26px;
  }
  .fill-name { position: absolute; left: 0; top: 20px; width: 100%; text-align: center; }
  .fill-rule { position: absolute; left: 10px; right: 10px; top: 94px; height: 1px; background: var(--ink); }
  .fill-divider { position: absolute; left: 168px; top: 94px; width: 1px; height: 66px; background: var(--ink); }
  .fill-abv { position: absolute; left: 10px; top: 104px; }
  .fill-date { position: absolute; left: 176px; top: 104px; }
  .volume {
    position: absolute; left: 0; top: 710px; width: 100%; text-align: center;
    font-family: "Arimo", Arial, sans-serif; font-size: 24px; line-height: 28px;
  }

  /* Back */
  .warning {
    position: absolute; left: 0; top: 308px; width: 100%; text-align: center;
    font-family: "Roboto Slab", Georgia, serif; font-weight: 300; font-size: 15px; line-height: 22px;
  }
  .maker { position: absolute; left: 80px; top: 580px; width: 300px; height: 90px; }
  .maker-mark { position: absolute; left: 25px; top: 0; width: 50px; height: 50px; border-radius: 50%; background: var(--ink); }
  .maker-name {
    position: absolute; left: 0; top: 56px; width: 100px; text-align: center;
    font-family: "Arimo", Arial, sans-serif; font-weight: 700; font-size: 12px; line-height: 15px;
  }
  .maker-address {
    position: absolute; left: 112px; top: 2px; white-space: nowrap;
    font-family: "Arimo", Arial, sans-serif; font-size: 16px; line-height: 22px; letter-spacing: .5px;
  }
  .website {
    position: absolute; left: 0; top: 680px; width: 100%; text-align: center;
    font-family: "Arimo", Arial, sans-serif; font-size: 17px; line-height: 22px; letter-spacing: 1px;
  }
</style>
</head>
<body>
<main class="sheet">
  <section class="panel panel--front">
    <div class="brand-mark" aria-hidden="true"></div>
    <div class="brand-name">FERN HOLLOW</div>
    <div class="brand-sub">ALES</div>
    <div class="brand-place">KESTREL COVE, ALASKA</div>
    <div class="crowler-band">CROWLER</div>
    <div class="fill-box">
      <div class="fill-name">Name:</div>
      <div class="fill-rule"></div>
      <div class="fill-divider"></div>
      <div class="fill-abv">ABV:</div>
      <div class="fill-date">Date:</div>
    </div>
    <div class="volume">32 FL.OZ</div>
  </section>

  <section class="panel panel--back">
    <p class="warning">
      GOVERNMENT WARNING:<br>
      (1) According to the Surgeon<br>
      General, women should not<br>
      drink alcoholic beverages<br>
      during pregnancy because of<br>
      the risk of birth defects.<br>
      (2) Consumption of alcoholic<br>
      beverages impairs your ability<br>
      to drive a car or operate<br>
      machinery,and may cause<br>
      health problems.
    </p>
    <div class="maker">
      <div class="maker-mark" aria-hidden="true"></div>
      <div class="maker-name">FERN HOLLOW ALES</div>
      <div class="maker-address">267 Tamarack Ln,<br>Kestrel Cove Alaska<br>99000</div>
    </div>
    <div class="website">www.fernhollowales.com</div>
  </section>
</main>
</body>
</html>
```